Need Stunning Website for Talent Acquisition (Recruiting) Agency

Hello, I am seeking a very professional, high-quality website that reflects our Talent Acquisition agency, Kindred Hires. Our agency slogan is "Talent Acquisition. Differently." We are in fact different - we are a full service agency that provides services most others do not, and our website needs to immediately reflect that something is different about us when they visit our site.

This contest is to do complete website design and coding, including all graphics, features, plugins, and design elements. The graphics are very important on the site and must be of the highest professional quality. One critical aspect is that the imagery must convey that we serve clients in a variety of industries, including business, healthcare, churches and religious organizations, non-profits, manufacturing, retail, and more. We recruit for both professional level positions (e.g. CEO, COO, Pastor), as well as entry level (e.g. secretary, caregiver, factory worker).
The following pages should be designed:
Home Page - a captivating home page that immediately tells our brand story, what makes us different, and the value that we bring to the table.
Client Services Page - a page that talks more about the services we provide and why we produce better results. This page will cover the 5 C's in greater detail as well as all the things that make us different.
Industries - The industries we serve
Request Services - a page where clients can submit details about a job they would like us to recruit for, including attaching a job description if they have one
Candidates Page - a simple page that encourages prospective candidates to submit their resume for review
About Us - Common about us page
Blog - Common blog page
Contact Us - a contact page for general inquiries
The website must be built in an ultra-SEO friendly manner and optimized for speed and performance. As mentioned above, you will be responsible for providing all graphics for the site (copyright compliant).
The website will need to be compatible with Elementor Pro (I have subscription) and Yoast SEO. It needs to be designed on a high-quality wordpress theme that receives regular updates. It also needs instant chat messaging feature. Would like a traditional menu bar at the top of the page (not a fan of menu's that are hidden or put on the side of the page).

Please, please, please - - do NOT waste my time with generic/stock templates, low-quality graphics, etc. We are a PREMIUM agency and our website needs to reflect that.

In the future we will add a job board - I do not want that initially - but will want the option to add it later.

Must also have the ability to upload documents /attachments on the contact page/form.

It probably goes without saying, but the page must be fully responsive - suitable to work on all device types.

Target Market(s)

Businesses

Industry/Entity Type

Talent Acquisition (Recruiting) Agency

Coding

Coded - Design and coding required

Number of Pages Required

5+ page

Requirements
Must have
• Please see brief
Should not have
• No generic template/stock website or graphics - must have PREMIUM feel.

```html
<!DOCTYPE html>
<html lang="en">
<head>
<meta charset="utf-8">
<title>Testimonials — Kindred Hires</title>
<link href="https://fonts.googleapis.com/css2?family=Inter:wght@500&family=Poppins:wght@400;600&display=swap" rel="stylesheet">
<style>
  :root {
    --page-bg: #f8f8f8;
    --card-bg: #ffffff;
    --eyebrow: #1a72c2;
    --heading: #111a48;
    --name: #151515;
    --body: #1c1c1c;
    --star: #f6b500;
  }
  * { margin: 0; padding: 0; box-sizing: border-box; }
  html, body { width: 1200px; height: 755px; overflow: hidden; }
  body {
    background: var(--page-bg);
    font-family: "Poppins", sans-serif;
    position: relative;
  }
  .section-eyebrow {
    position: absolute; top: 75px; left: 0; width: 1200px;
    text-align: center; color: var(--eyebrow);
    font-size: 13px; font-weight: 400; letter-spacing: 3.6px;
  }
  .section-title {
    position: absolute; top: 104px; left: 0; width: 1200px;
    text-align: center; color: var(--heading);
    font-size: 41px; font-weight: 600; line-height: 51px; letter-spacing: -0.3px;
  }
  .review-card {
    position: absolute; width: 297px;
    background: var(--card-bg);
    padding: 17px 17px 0 17px;
  }
  .reviewer { display: flex; align-items: flex-start; gap: 7px; height: 58px; }
  .reviewer-photo {
    width: 40px; height: 40px; border-radius: 50%; flex: none;
    background: radial-gradient(circle at 50% 40%, #b08a70 0 35%, #5d6a78 70%, #cfd3d8 100%);
  }
  .reviewer-name {
    font-family: "Inter", sans-serif; font-weight: 500;
    font-size: 13px; color: var(--name); margin-top: 2px;
  }
  .rating { display: flex; gap: 8.6px; margin-top: 9px; margin-left: 2px; }
  .rating svg { width: 9px; height: 9px; fill: var(--star); }
  .review-text {
    font-size: 12px; line-height: 20.9px; color: var(--body);
    margin-top: 3px;
  }
</style>
</head>
<body>
  <svg width="0" height="0" style="position:absolute">
    <defs>
      <symbol id="star" viewBox="0 0 24 24"><path d="M12 1.5l3.1 7 7.6.7-5.8 5 1.8 7.5L12 17.8l-6.7 3.9 1.8-7.5-5.8-5 7.6-.7z"/></symbol>
    </defs>
  </svg>

  <p class="section-eyebrow">TESTIMONIAL</p>
  <h1 class="section-title">See what they’re<br>saying about us</h1>

  <article class="review-card" style="left:136px;top:242px;height:211px">
    <div class="reviewer">
      <div class="reviewer-photo" role="img" aria-label="Portrait photo of Mara Whitcombe"></div>
      <div><p class="reviewer-name">Mara Whitcombe</p>
        <div class="rating"><svg><use href="#star"/></svg><svg><use href="#star"/></svg><svg><use href="#star"/></svg><svg><use href="#star"/></svg><svg><use href="#star"/></svg></div></div>
    </div>
    <p class="review-text">I have been using Kindred Hires for quite some time now and I have to say it has been the best freelance hiring platform that I've used. The quality of freelancers on this site is very high and they're totally reliable. I would highly recommend it!</p>
  </article>

  <article class="review-card" style="left:136px;top:474px;height:233px">
    <div class="reviewer">
      <div class="reviewer-photo" role="img" aria-label="Portrait photo of Lena Corrick" style="background:radial-gradient(circle at 50% 40%,#8a5a3e 0 35%,#5a2e1c 70%,#c9a6b8 100%)"></div>
      <div><p class="reviewer-name">Lena Corrick</p>
        <div class="rating"><svg><use href="#star"/></svg><svg><use href="#star"/></svg><svg><use href="#star"/></svg><svg><use href="#star"/></svg><svg><use href="#star"/></svg></div></div>
    </div>
    <p class="review-text">One of the best things about Kindred Hires is that it really simplifies the process of finding and hiring people. The quality is good as well, every freelancer I've hired has been high-quality and professional. I would recommend this to anyone who needs a freelancer.</p>
  </article>

  <article class="review-card" style="left:453px;top:242px;height:191px">
    <div class="reviewer">
      <div class="reviewer-photo" role="img" aria-label="Portrait photo of Dorian Vale" style="background:radial-gradient(circle at 50% 40%,#b88468 0 35%,#3a3a3a 70%,#d8d8d8 100%)"></div>
      <div><p class="reviewer-name">Dorian Vale</p>
        <div class="rating"><svg><use href="#star"/></svg><svg><use href="#star"/></svg><svg><use href="#star"/></svg><svg><use href="#star"/></svg><svg><use href="#star"/></svg></div></div>
    </div>
    <p class="review-text">I’m so happy because the freelance talent we work with are more productive than we have ever thought. Recommend for people who want to find professional freelancer on this platform.</p>
  </article>

  <article class="review-card" style="left:453px;top:453px;height:275px">
    <div class="reviewer">
      <div class="reviewer-photo" role="img" aria-label="Portrait photo of Jonah Pell" style="background:radial-gradient(circle at 50% 40%,#6b4634 0 35%,#1e2a3a 70%,#e2e2e2 100%)"></div>
      <div><p class="reviewer-name">Jonah Pell</p>
        <div class="rating"><svg><use href="#star"/></svg><svg><use href="#star"/></svg><svg><use href="#star"/></svg><svg><use href="#star"/></svg><svg><use href="#star"/></svg></div></div>
    </div>
    <p class="review-text">&nbsp;have used a lot of freelance hiring platforms, but none compare to Kindred Hires. The quality of freelancers that I can find here is unmatched and the service is top-notch. The customer service is also excellent, which cannot be said for my previous experiences in using other apps. I would highly recommend this product for anyone looking to hire a freelancer.</p>
  </article>

  <article class="review-card" style="left:771px;top:242px;height:232px">
    <div class="reviewer">
      <div class="reviewer-photo" role="img" aria-label="Portrait photo of Felix Ortane" style="background:radial-gradient(circle at 50% 40%,#8e6048 0 35%,#2e3440 70%,#6e7780 100%)"></div>
      <div><p class="reviewer-name">Felix Ortane</p>
        <div class="rating"><svg><use href="#star"/></svg><svg><use href="#star"/></svg><svg><use href="#star"/></svg><svg><use href="#star"/></svg><svg><use href="#star"/></svg></div></div>
    </div>
    <p class="review-text">I am happy to say that I have hired a couple of freelancers through &nbsp;and they are high-quality ones. Working with them is not just easier; it has also been more effective. Having found a great freelance team, I cannot imagine switching to any other hiring platform.</p>
  </article>

  <article class="review-card" style="left:771px;top:495px;height:233px">
    <div class="reviewer">
      <div class="reviewer-photo" role="img" aria-label="Portrait photo of Simon Arlow" style="background:radial-gradient(circle at 50% 40%,#9a6a50 0 30%,#9fb6cc 65%,#eef2f6 100%)"></div>
      <div><p class="reviewer-name">Simon Arlow</p>
        <div class="rating"><svg><use href="#star"/></svg><svg><use href="#star"/></svg><svg><use href="#star"/></svg><svg><use href="#star"/></svg><svg><use href="#star"/></svg></div></div>
    </div>
    <p class="review-text">I have used a number of different freelance hiring platforms and none come close to Kindred Hires. The quality of the freelancers on here is top notch and it's easy to browse through the listings. I've been using it for six months now and I've found my perfect freelancer without any regrets whatsoever.</p>
  </article>
</body>
</html>
```